Communication and Marketing agency needs a new presentation card

We are a group of communication and marketing agencies specialized in companies that are in the logistics and industrial sector. The head agency is TELVANO Grupo and the group consists of 4 agencies: TELVANO Media, TELVANO Digital, TELVANO Research and EnlazaPorImagen. We hace 4 offices in Spain (Madrid, Barcelona, Valencia and Murcia). We are looking for a clean and attractive design that transmits our experience, brand presence in the market and knowledge to those who receive the card.It has to maintain the colors of the logo that is attached.
Target Market(s)
logistics and industrial sector
Marketing department
Clean and attractive design

```html
<!DOCTYPE html>
<html lang="es">
<head>
<meta charset="utf-8">
<title>TELVANO Grupo – Business Card</title>
<link rel="stylesheet" href="https://fonts.googleapis.com/css2?family=Open+Sans:wght@400;600&family=Roboto:wght@700&display=swap">
<style>
  :root {
    --bg: #2a2a2a;
    --card-light: #eeeeee;
    --brand-red: #b01c27;
    --band-grey: #524d4a;
    --text-dark: #3a3a3a;
    --rule: #9a9a9a;
    --white: #ffffff;
  }
  * { box-sizing: border-box; margin: 0; padding: 0; }
  html, body { width: 1200px; height: 1200px; overflow: hidden; }
  body {
    background: var(--bg);
    position: relative;
    font-family: "Open Sans", Arial, sans-serif;
  }
  .card {
    position: absolute;
    top: 310px;
    width: 366px;
    height: 594px;
  }
  .card--front { left: 233px; background: var(--card-light); }
  .card--back { left: 628px; background: var(--brand-red); }

  .wordmark {
    position: absolute;
    left: 0; right: 0;
    text-align: center;
    font-family: "Open Sans", Arial, sans-serif;
    font-weight: 600;
    line-height: 1;
  }
  .wordmark__name { display: block; font-size: 48px; letter-spacing: 2px; }
  .wordmark__sub { display: block; font-size: 30px; margin-top: 6px; padding-left: 140px; }
  .card--front .wordmark { top: 142px; color: var(--brand-red); }
  .card--back .wordmark { top: 158px; color: var(--white); }

  .contact {
    position: absolute;
    top: 336px; left: 0; right: 0;
    text-align: center;
    color: var(--text-dark);
  }
  .contact__name {
    font-family: "Roboto", Arial, sans-serif;
    font-weight: 700;
    font-size: 25px;
    color: var(--brand-red);
    letter-spacing: 0.3px;
  }
  .contact__role { font-size: 17px; margin-top: 2px; }
  .contact__rule {
    width: 208px; height: 1px;
    background: var(--rule);
    margin: 9px auto 11px;
  }
  .contact__line { font-size: 17px; line-height: 21.7px; }
  .contact__label { color: var(--brand-red); font-weight: 600; }
  .contact__web { color: var(--brand-red); font-weight: 600; font-size: 17px; line-height: 22px; }

  .offices {
    position: absolute;
    top: 307px; left: 0; right: 0;
    height: 66px;
    background: var(--band-grey);
    color: var(--white);
    font-size: 17px;
    display: flex; align-items: center; justify-content: center;
    letter-spacing: 0.2px;
  }

  .agencies {
    position: absolute;
    top: 448px; left: 42px; right: 42px;
    display: grid;
    grid-template-columns: 1fr 1fr;
    row-gap: 24px;
    column-gap: 14px;
    color: var(--white);
    font-weight: 600;
    text-align: center;
  }
  .agency { line-height: 1.05; }
  .agency__name { display: block; font-size: 19px; letter-spacing: 0.5px; }
  .agency__sub { display: block; font-size: 13px; padding-left: 46px; }
  .agency--solo .agency__name { font-size: 17px; padding-top: 8px; letter-spacing: 0; }
</style>
</head>
<body>
  <section class="card card--front" aria-label="Front of business card">
    <div class="wordmark">
      <span class="wordmark__name">TELVANO</span>
      <span class="wordmark__sub">Grupo</span>
    </div>
    <div class="contact">
      <h1 class="contact__name">MARCOS ELVERDI</h1>
      <p class="contact__role">Managing Director</p>
      <div class="contact__rule"></div>
      <p class="contact__line"><span class="contact__label">P:</span> 091-482 305 617</p>
      <p class="contact__line"><span class="contact__label">M:</span> 091-482 305 618</p>
      <p class="contact__line"><span class="contact__label">E:</span> hola@telvano.es</p>
      <p class="contact__web">www.telvanogrupo.es</p>
      <div class="contact__rule"></div>
      <p class="contact__line">28014, Calle del Puerto 18</p>
      <p class="contact__line">Madrid, España.</p>
    </div>
  </section>

  <section class="card card--back" aria-label="Back of business card">
    <div class="wordmark">
      <span class="wordmark__name">TELVANO</span>
      <span class="wordmark__sub">Grupo</span>
    </div>
    <div class="offices">Madrid, Barcelona, Valencia, Murcia</div>
    <div class="agencies">
      <div class="agency"><span class="agency__name">TELVANO</span><span class="agency__sub">Research</span></div>
      <div class="agency"><span class="agency__name">TELVANO</span><span class="agency__sub">Digital</span></div>
      <div class="agency"><span class="agency__name">TELVANO</span><span class="agency__sub">Media</span></div>
      <div class="agency agency--solo"><span class="agency__name">EnlazaPorImagen</span></div>
    </div>
  </section>
</body>
</html>
```